Lumo Fortunado superhero master

Full website makeover/update and redesign About a Public Figure.. in Spanish as well as English.
See current website at LumoFortunado.example and Chatterbook page LumoFortunates .
you can use any of the pictures and videos and be creative. page will be in English and Spanish same design.
think about a Zen Superhero, like Kael from the lattice, with secret mystic knowledge, a combination of the character "Captain Vesper" mixed with the Millionaire Falcon of Harbor Row. Themes related to Mentor, based on zodiac, about Financial abundance using the stock Market.

Reason: designs are not what I like

Target Market(s)

USA hispanics Market

Number of Pages Required

5+ page

Colors

Designer to choose colors to be used in the design.

Requirements
Must have
• think about a Zen Superhero, like Kael from the lattice, with secret mystic knowledge, a combination of the character "Captain Vesper" mixed with the Millionaire Falcon of Harbor Row. Themes related to Mentor, based on zodiac, about Financial abundance using the stock Market. Surprise me :)
Nice to have
• think about a Zen Superhero, like Kael from the lattice, with secret mystic knowledge, a combination of the character "Captain Vesper" mixed with the falcon of harbor row.

```html
<!DOCTYPE html>
<html lang="en">
<head>
<meta charset="utf-8">
<title>LumoFortunates</title>
<link rel="stylesheet" href="https://fonts.googleapis.com/css2?family=Roboto:wght@400;500;700&family=Open+Sans:wght@400;600;700&display=swap">
<style>
:root{
  --orange:#f39221;
  --orange-deep:#ef8417;
  --green:#5cad2f;
  --green-dark:#3f8a1c;
  --ink:#222;
  --text:#555;
  --muted:#888;
  --light:#f3f2f2;
  --line:#d9d9d9;
  --navy:#0d1733;
  --white:#fff;
}
*{box-sizing:border-box;margin:0;padding:0}
html,body{width:1200px;height:3249px;overflow:hidden}
body{position:relative;background:var(--white);font-family:"Open Sans",Arial,sans-serif;color:var(--text)}
.abs{position:absolute}
.btn{position:absolute;display:flex;align-items:center;justify-content:center;background:var(--green);color:var(--white);font:700 12px "Roboto",Arial,sans-serif;letter-spacing:.5px;border-radius:3px;border-bottom:4px solid var(--green-dark)}
/* top bar */
.topbar{top:0;left:0;width:1200px;height:30px;font-size:11px;color:#444}
.topbar .lang{left:200px;top:8px}
.topbar .mail{left:288px;top:8px}
.topbar .social{left:925px;top:9px;display:flex;gap:8px}
.topbar .social span{width:11px;height:11px;border-radius:50%;background:#555;display:block}
/* header */
.brand{left:200px;top:48px;display:flex;align-items:center;gap:12px}
.brand .mark{width:34px;height:44px;background:var(--orange)}
.brand .name{font:700 26px "Roboto",Arial,sans-serif;color:var(--orange);letter-spacing:-.5px}
.contact{display:flex;align-items:center;gap:18px;top:52px}
.contact .ico{width:40px;height:40px;border:1px solid #ccc;border-radius:3px;display:flex;align-items:center;justify-content:center}
.contact b{display:block;font:500 16px "Roboto",Arial,sans-serif;color:var(--ink)}
.contact small{font-size:11px;color:var(--muted)}
.support{left:676px}.call{left:874px}
.vsep{left:838px;top:50px;width:1px;height:44px;background:#ddd}
/* nav */
.nav{top:122px;left:0;width:1200px;height:34px;border-top:1px solid var(--line);border-bottom:1px solid var(--line)}
.nav a{position:absolute;top:10px;font:500 11.5px "Roboto",Arial,sans-serif;color:#333;text-decoration:none;letter-spacing:.4px}
.nav .search{left:862px;top:6px;width:138px;height:20px;border-bottom:1px solid #333;font:500 11px "Roboto",Arial,sans-serif;color:#333;padding-top:4px}
.nav .search svg{position:absolute;right:2px;top:3px}
/* hero */
.hero{top:160px;left:0;width:1200px;height:630px;background:radial-gradient(ellipse at 70% 35%,#3a2f6a 0%,#1a1f4a 35%,var(--navy) 70%),linear-gradient(180deg,#141b3e,#0a2a3a);text-align:center;color:var(--white)}
.hero .shade{inset:auto 0 0 0;height:260px;background:linear-gradient(180deg,rgba(10,40,60,0),rgba(20,90,110,.55))}
.hero .kicker{top:155px;left:0;width:1200px;font:400 30px "Roboto",Arial,sans-serif;letter-spacing:1px}
.hero .div{top:224px;left:372px;width:456px;height:8px}
.hero h1{top:280px;left:0;width:1200px;font:700 38px/60px "Roboto",Arial,sans-serif;letter-spacing:-.3px}
.hero h1 em{font-style:normal;color:var(--orange)}
.hero .cta{top:440px;left:509px;width:179px;height:50px;border:1px solid rgba(255,255,255,.8);border-radius:4px;display:flex;align-items:center;justify-content:center;font:500 15px "Roboto",Arial,sans-serif;background:rgba(255,255,255,.08)}
.arrow{top:308px;width:36px;height:36px;border-radius:50%;background:var(--white);display:flex;align-items:center;justify-content:center}
/* steps */
.steps{top:797px;left:0;width:1200px;height:173px;background:var(--light)}
.step{top:44px;width:260px;display:flex;gap:14px}
.step .num{width:46px;text-align:center}
.step .num span{display:flex;width:46px;height:40px;background:var(--green);color:var(--white);font:700 22px "Roboto",Arial,sans-serif;align-items:center;justify-content:center}
.step .num small{font:700 11px "Roboto",Arial,sans-serif;color:var(--ink)}
.step h3{font:700 13.5px/18px "Open Sans",Arial,sans-serif;color:var(--ink)}
.step p{font-size:12.5px;line-height:18px;color:#666;margin-top:2px}
/* section headings */
.sec-title{left:0;width:1200px;text-align:center;font:500 28px "Roboto",Arial,sans-serif;color:var(--ink);letter-spacing:.3px}
.divider{left:405px;width:390px;height:30px}
.alerts-copy{top:1168px;left:200px;width:800px;text-align:center;font-size:12.5px;line-height:24px;color:#666}
/* trades */
.trades{top:1393px;left:0;width:1200px;height:492px;background:linear-gradient(90deg,#3b3f46 0%,#4a4f57 45%,#2a3340 70%,#1d2632 100%)}
.trades .veil{inset:0;background:rgba(20,22,28,.45)}
.table{top:178px;left:390px;width:420px;border-collapse:collapse;color:var(--white);font-size:12px}
.table th{font:700 12.5px "Roboto",Arial,sans-serif;text-align:left;padding:0 6px 8px;border-bottom:1px solid rgba(255,255,255,.6)}
.table td{padding:3px 6px;height:23px;white-space:nowrap}
/* service rows */
.photo{position:absolute}
.label{font:500 11.5px "Roboto",Arial,sans-serif;color:var(--ink);border-left:2px solid var(--orange);padding-left:10px;letter-spacing:.3px}
.label b{display:block;font:700 28px/34px "Roboto",Arial,sans-serif;margin-top:2px}
.svc-copy{font-size:12.5px;line-height:21.5px;color:#555;width:370px}
/* footer */
.footer{top:2928px;left:0;width:1200px;height:261px;background:var(--orange)}
.footer h4{position:absolute;top:56px;font:700 17px "Roboto",Arial,sans-serif;color:var(--white);letter-spacing:.4px}
.footer p,.footer li{font-size:12px;line-height:20px;color:var(--white)}
.footer ul{list-style:none}
.footer li::before{content:"›";margin-right:8px}
.f-about{left:200px}.f-links{left:540px}.f-news{left:780px}
.news-input{top:148px;left:780px;width:172px;height:36px;background:var(--white);font-size:10px;color:#aaa;padding:12px 0 0 18px}
.news-btn{top:148px;left:952px;width:40px;height:36px;background:var(--green);display:flex;align-items:center;justify-content:center}
.f-social{top:200px;left:780px;display:flex;gap:10px}
.f-social span{width:26px;height:26px;border:1px solid var(--white);border-radius:50%;display:block}
.bottombar{top:3189px;left:0;width:1200px;height:60px;background:var(--orange-deep);border-top:1px solid rgba(255,255,255,.35);font-size:11px;color:var(--white)}
</style>
</head>
<body>

<div class="abs topbar">
  <span class="abs lang">Language &#9662;</span>
  <span class="abs mail">&#9993;&nbsp; info@lumofortunates.example</span>
  <div class="abs social"><span></span><span></span><span></span><span></span></div>
</div>

<div class="abs brand"><span class="mark"></span><span class="name">LUMO FORTUNATES!</span></div>

<div class="abs contact support">
  <span class="ico"><svg width="20" height="20" viewBox="0 0 20 20"><circle cx="10" cy="10" r="8" fill="none" stroke="#333" stroke-width="1.6"/><path d="M10 5v5l3 2" fill="none" stroke="#333" stroke-width="1.6"/></svg></span>
  <div><b>Support</b><small>24 / 7 Hours</small></div>
</div>
<div class="abs vsep"></div>
<div class="abs contact call">
  <span class="ico"><svg width="20" height="20" viewBox="0 0 20 20"><path d="M5 2l3 4-2 2c1 2 3 4 5 5l2-2 4 3-2 3C9 17 3 11 2 4z" fill="#333"/></svg></span>
  <div><b>Call</b><small>(555) 014-2290</small></div>
</div>

<nav class="abs nav">
  <a style="left:200px">HOME</a>
  <a style="left:282px">SIGN UP!</a>
  <a style="left:381px">HOW IT WORKS</a>
  <a style="left:511px">ABOUT LUMO</a>
  <a style="left:632px">VIDEOS</a>
  <a style="left:728px">F.A.Q.</a>
  <div class="abs search">SEARCH<svg width="12" height="12" viewBox="0 0 12 12"><circle cx="5" cy="5" r="3.8" fill="none" stroke="#333" stroke-width="1.4"/><path d="M8 8l3 3" stroke="#333" stroke-width="1.4"/></svg></div>
</nav>

<section class="abs hero" role="img" aria-label="Dark trading floor background with glowing stock chart lines and ticker figures">
  <div class="abs shade"></div>
  <p class="abs kicker">THINK BIG</p>
  <svg class="abs div" viewBox="0 0 456 8"><line x1="0" y1="4" x2="190" y2="4" stroke="rgba(255,255,255,.5)"/><line x1="266" y1="4" x2="456" y2="4" stroke="rgba(255,255,255,.5)"/><circle cx="214" cy="4" r="3.5" fill="#f39221"/><circle cx="228" cy="4" r="3.5" fill="#f39221"/><circle cx="242" cy="4" r="3.5" fill="#f39221"/></svg>
  <h1 class="abs">I TURNED THE STOCK MARKET &nbsp;INTO<br><em>MY SOURCE OF INCOME!</em></h1>
  <div class="abs cta">GET STARTED TODAY</div>
  <span class="abs arrow" style="left:79px"><svg width="10" height="12" viewBox="0 0 10 12"><path d="M8 1L2 6l6 5" fill="none" stroke="#222" stroke-width="2"/></svg></span>
  <span class="abs arrow" style="left:1085px"><svg width="10" height="12" viewBox="0 0 10 12"><path d="M2 1l6 5-6 5" fill="none" stroke="#222" stroke-width="2"/></svg></span>
</section>

<section class="abs steps">
  <div class="abs step" style="left:200px"><div class="num"><span>1.</span><small>STEP</small></div><div><h3>Learn the Right Way to Trade Stock</h3><p>Lorem Ipsum is simply dummy text of the printing....</p></div></div>
  <div class="abs step" style="left:472px"><div class="num"><span>2.</span><small>STEP</small></div><div><h3>Practice on a Demo Account &amp; See My Alerts</h3><p>Lorem Ipsum is simply dummy text of the printing....</p></div></div>
  <div class="abs step" style="left:762px"><div class="num"><span>3.</span><small>STEP</small></div><div><h3>Earn Thousands and Enjoy the Life you Deserve</h3><p>Lorem Ipsum is simply dummy text of the printing....</p></div></div>
</section>

<h2 class="abs sec-title" style="top:1038px">8 OUT OF 10 OF MY ALERTS GO UP 20% SAME DAY</h2>
<svg class="abs divider" style="top:1106px" viewBox="0 0 390 30"><line x1="0" y1="18" x2="165" y2="18" stroke="#f39221" stroke-width="1.5"/><line x1="225" y1="18" x2="390" y2="18" stroke="#f39221" stroke-width="1.5"/><g fill="#f39221"><rect x="182" y="16" width="5" height="10"/><rect x="190" y="12" width="5" height="14"/><rect x="198" y="8" width="5" height="18"/></g><path d="M180 14l8-6 6 4 12-9" fill="none" stroke="#f39221" stroke-width="2"/></svg>
<p class="abs alerts-copy">Did you know that today over 50 different companies on the stock market went up 20-300%? This happens every day and I can show you how to turn the Stock Market into your own private business. My goal is to help you make more money. LumoFortunate's goal is to help those ready to become independent &amp; financially free, even if you are low on funds. He is posting 1-2 FREE Alerts weekly on our Chatterbook page....</p>
<div class="btn" style="top:1291px;left:537px;width:124px;height:40px">READ MORE</div>

<section class="abs trades" role="img" aria-label="Businessman's hand over a tablet with a night city skyline, dimmed behind the trades table">
  <div class="abs veil"></div>
  <h2 class="abs sec-title" style="top:60px;color:#fff">LUMOFORTUNATE'S&nbsp; LASTEST&nbsp; TRADES</h2>
  <svg class="abs divider" style="top:114px" viewBox="0 0 390 30"><line x1="0" y1="18" x2="165" y2="18" stroke="#f39221" stroke-width="1.5"/><line x1="225" y1="18" x2="390" y2="18" stroke="#f39221" stroke-width="1.5"/><g fill="#f39221"><rect x="182" y="16" width="5" height="10"/><rect x="190" y="12" width="5" height="14"/><rect x="198" y="8" width="5" height="18"/></g><path d="M180 14l8-6 6 4 12-9" fill="none" stroke="#f39221" stroke-width="2"/></svg>
  <table class="abs table">
    <tr><th>DATE</th><th>STOCK</th><th>ENTRY</th><th>EXIT</th><th>PROFIT</th></tr>
    <tr><td>8/29</td><td>QZVA</td><td>$&nbsp;&nbsp; 0.43</td><td>$&nbsp;&nbsp; 0.55</td><td>$ 1,440.00</td></tr>
    <tr><td>8/28</td><td>MOLR</td><td>$&nbsp;&nbsp; 0.31</td><td>$&nbsp;&nbsp; 0.35</td><td>$&nbsp;&nbsp;&nbsp; 637.00</td></tr>
    <tr><td>8/28</td><td>DXKE</td><td>$&nbsp;&nbsp; 0.12</td><td>$&nbsp;&nbsp; 0.14</td><td>$ 1,416.00</td></tr>
    <tr><td>8/24</td><td>LTVW</td><td>$&nbsp;&nbsp; 2.42</td><td>$&nbsp;&nbsp; 2.37</td><td>$&nbsp; (310.00)</td></tr>
    <tr><td>8/23</td><td>OPQZ</td><td>$&nbsp;&nbsp; 1.08</td><td>$&nbsp;&nbsp; 1.12</td><td>$&nbsp;&nbsp;&nbsp; 240.00</td></tr>
  </table>
  <div class="btn" style="top:394px;left:538px;width:124px;height:40px">VIEW ALL</div>
</section>

<div class="photo" style="top:1971px;left:0;width:600px;height:438px;background:linear-gradient(135deg,#cfd6dc 0%,#8a98a6 45%,#3e4a57 100%)" role="img" aria-label="Hands holding a tablet showing a stock chart"></div>
<div class="abs" style="top:1971px;left:600px;width:600px;height:438px;background:var(--light)"></div>
<div class="abs label" style="top:2015px;left:628px">MOST POPULAR SERVICE<b>LUMO ALERTS!</b></div>
<p class="abs svc-copy" style="top:2090px;left:655px">With LumoAlerts*** you know exactly when I get inandout of my trades. Take advantage of the FreeTrainingclass- for subscribers, a great tool for new traders or thoswith some experience. You can expect 1-3 Alerts per day on Stocks under $10. LumoFortunate is always trading stocks with strong breakout characteristics and a strong profile that match my 4 tested Indicators. Is not uncommon for my trades to gain 25-50% in a single day (sometimes in a single hour. Check some of my past trades, the FAQ&nbsp; and How it Works).</p>
<div class="btn" style="top:2318px;left:656px;width:122px;height:42px">READ MORE</div>

<div class="abs label" style="top:2454px;left:223px">MOST POPULAR SERVICE<b>LUMO COACH!</b></div>
<p class="abs svc-copy" style="top:2530px;left:224px">Is not about the Money. Is about your super power! That's the secret you learn One on One with The LumoFortunate. With a personalized analysis covering the Law of Attraction in your life, LumoFortunate pinpoints the subconscious blocks that are holding you back from creating abundance. But you will receive more detailed training and Alerts. This is the roadmap to becoming a Millionaire trader. One time payment includes a Lifetime of extended LumoVipAlerts, Private one on one mentorship, learning &amp; trading live with the best.</p>
<div class="btn" style="top:2760px;left:225px;width:124px;height:42px">READ MORE</div>
<div class="photo" style="top:2409px;left:602px;width:598px;height:440px;background:linear-gradient(100deg,#f4f4f4 0%,#e6e6e6 40%,#9aa0a8 75%,#2b2f36 100%)" role="img" aria-label="Businessman in a suit holding a clipboard with a market shares bar chart"></div>

<footer class="abs footer">
  <h4 class="f-about">ABOUT LUMO</h4>
  <div class="abs f-about" style="top:92px;width:250px">
    <p>I have been born more than once so I have many names but this story began with a spiritual journey from deep within the heart of Cuba, patterns...</p>
    <p>Call : (555) 014-2290</p>
    <p>E-mail : info@lumofortunates.example</p>
  </div>
  <h4 class="f-links">USEFUL LINKS</h4>
  <ul class="abs f-links" style="top:92px"><li>Home</li><li>Sign Up!</li><li>How It Work</li><li>About Lumo</li><li>Videos</li></ul>
  <h4 class="f-news">NEWSLETTER</h4>
  <p class="abs f-news" style="top:92px;width:210px">Lorem Ipsum is simply dummy text of the printing&nbsp; industry.</p>
  <div class="abs news-input">ENTER MAIL</div>
  <div class="abs news-btn"><svg width="16" height="12" viewBox="0 0 16 12"><path d="M0 6h14M9 1l5 5-5 5" fill="none" stroke="#fff" stroke-width="2"/></svg></div>
  <div class="abs f-social"><span></span><span></span><span></span><span></span></div>
</footer>
<div class="abs bottombar">
  <span class="abs" style="left:200px;top:24px">Copyright ©2017 lumofortunates.&nbsp; All Rights Reserved</span>
  <span class="abs" style="left:722px;top:24px">Privacy Policy&nbsp; |&nbsp; Terms And Conditions&nbsp; |&nbsp; Support</span>
</div>

</body>
</html>
```